Velvet Oaks rebranding my business with a new business card

I have my new logo and now I need a refresher on my business cards. I really want something fun and fresh. I like black background or anything to make the color pop.
Logo
Name: Velvet Oaks
Contact Info as stated below:
Mira Calloway
647-382-9164
Logo
Name: Velvet Oaks
Mira Calloway
647-382-9164
fb.me/VelvetOaksbyMira
Instagram: @VelvetOaksbyMira

Industry/Entity Type

Business

Contact Information for Business Card

double-sided. Logo on one side. Contact info on the other.

Requirements
Must have
• Logo
• Name: Velvet Oaks
• Contact Info as stated below:
• Mira Calloway
• 647-382-9164
• fb.me/VelvetOaksbyMira
• fb.me/VelvetOaksbyMira

```html
<!DOCTYPE html>
<html lang="en">
<head>
<meta charset="utf-8">
<title>Velvet Oaks – Business Card</title>
<link rel="stylesheet" href="https://fonts.googleapis.com/css2?family=Kotta+One&family=Nunito:wght@400;600&display=swap">
<style>
  :root {
    --backdrop: #141414;
    --card: #1d1d1d;
    --cream: #efe4c4;
    --pink: #f2a9bd;
    --ring-pink: #e887c4;
    --teal: #4cc2b0;
    --ink: #1a1a1a;
  }
  * { box-sizing: border-box; margin: 0; padding: 0; }
  html, body {
    width: 1200px;
    height: 1000px;
    overflow: hidden;
    background: var(--backdrop);
  }
  .canvas {
    position: relative;
    width: 1200px;
    height: 1000px;
  }
  .card {
    position: absolute;
    top: 350px;
    width: 530px;
    height: 300px;
    border-radius: 18px;
    background: var(--card);
    overflow: hidden;
    box-shadow: 0 10px 30px rgba(0,0,0,0.45);
  }
  .card--contact { left: 50px; }
  .card--logo { left: 620px; }

  .brand {
    position: absolute;
    display: flex;
    align-items: center;
    gap: 12px;
  }
  .brand__dot {
    border-radius: 50%;
    background: var(--pink);
    flex: none;
  }
  .brand__name {
    font-family: "Kotta One", serif;
    color: var(--cream);
    white-space: nowrap;
  }
  .card--contact .brand { left: 36px; top: 48px; }
  .card--contact .brand__dot { width: 58px; height: 58px; }
  .card--contact .brand__name { font-size: 34px; }

  .holder {
    position: absolute;
    right: 34px;
    top: 142px;
    font-family: "Kotta One", serif;
    font-size: 26px;
    color: var(--cream);
  }
  .contact-bar {
    position: absolute;
    right: 0;
    height: 32px;
    border-radius: 16px 0 0 16px;
    display: flex;
    align-items: center;
    gap: 10px;
    padding-left: 5px;
    font-family: "Nunito", sans-serif;
    font-size: 20px;
    color: var(--ink);
  }
  .contact-bar--phone { top: 186px; width: 290px; background: var(--pink); }
  .contact-bar--social { top: 226px; width: 360px; background: var(--teal); }
  .contact-bar__icon {
    width: 24px;
    height: 24px;
    border-radius: 50%;
    background: var(--card);
    display: flex;
    align-items: center;
    justify-content: center;
    flex: none;
  }
  .contact-bar__icon svg { width: 14px; height: 14px; }

  .ring {
    position: absolute;
    inset: 0;
  }
  .card--logo .brand {
    left: 50%;
    top: 50%;
    transform: translate(-50%, -50%);
    flex-direction: column;
    gap: 14px;
  }
  .card--logo .brand__dot { width: 90px; height: 90px; }
  .card--logo .brand__name { font-size: 36px; }
</style>
</head>
<body>
<main class="canvas">

  <section class="card card--contact">
    <div class="brand">
      <span class="brand__dot"></span>
      <span class="brand__name">Velvet Oaks</span>
    </div>
    <p class="holder">Mira Calloway</p>
    <div class="contact-bar contact-bar--phone">
      <span class="contact-bar__icon">
        <svg viewBox="0 0 24 24"><path fill="#f2a9bd" d="M6.6 10.8a15.1 15.1 0 0 0 6.6 6.6l2.2-2.2a1 1 0 0 1 1-.25 11.4 11.4 0 0 0 3.6.57 1 1 0 0 1 1 1V20a1 1 0 0 1-1 1A17 17 0 0 1 3 4a1 1 0 0 1 1-1h3.5a1 1 0 0 1 1 1c0 1.25.2 2.45.57 3.57a1 1 0 0 1-.25 1z"/></svg>
      </span>
      <span>647-382-9164</span>
    </div>
    <div class="contact-bar contact-bar--social">
      <span class="contact-bar__icon"></span>
      <span>VelvetOaksbyMira</span>
    </div>
  </section>

  <section class="card card--logo">
    <svg class="ring" viewBox="0 0 530 300" aria-hidden="true">
      <circle cx="265" cy="150" r="190" fill="none" stroke="var(--ring-pink)" stroke-width="6"/>
      <circle cx="265" cy="150" r="178" fill="none" stroke="var(--ring-pink)" stroke-width="2"/>
    </svg>
    <div class="brand">
      <span class="brand__dot"></span>
      <span class="brand__name">Velvet Oaks</span>
    </div>
  </section>

</main>
</body>
</html>
```